Glasses Promo

I am an optometrist, and we want to get our contact lens buying patients into the habit if buying glasses, too. It's not healthy to be stranded in contact lenses, with no viable glasses options. This post-card sized card would be handed out to all patients that are purchasing contact lenses from the practice, offering a complete pair of glasses, including frames, Vorne lenses, and a one year warranty, starting at $59.
Suggestion for text: buy a year supply of contact lenses and get a complete pair of glasses (new frame, vorne lenses, 1 year warranty) for $59
Updates

Project is now guaranteed / committed.  :) Let's see what you've got!

Target Market(s)

18-40 mixed male / female, quality, 'affordable luxury'

Industry/Entity Type

Promo

Requirements
Must have
• our logo (either one), vorne logo. simple, clean, premium feel.
limit one pair per patient. it should have our address and website. (ideas/info at our website: pennrockoptic.com )
simple, clean, would like a visual reference to glasses, either outline, silhouette, abstract, whatnot. be creative! :)
Nice to have
• frendlio quillo and m+ logos
Should not have
• dinosaurs. although they are awesome.

```html
<!DOCTYPE html>
<html lang="en">
<head>
<meta charset="utf-8">
<title>Pennrock Optic Associates – Glasses Promo Postcard</title>
<link rel="stylesheet" href="https://fonts.googleapis.com/css2?family=Questrial&family=Arimo:wght@400;700&display=swap">
<style>
  :root {
    --bg: #ece9e4;
    --card: #ffffff;
    --purple: #6b2370;
    --grey-text: #333333;
    --grey-mid: #7d7d7d;
    --rule: #9a9a9a;
    --partner-blue: #2f4fa2;
    --photo-light: #d9c7b0;
    --photo-dark: #6b5a4a;
    --illus-light: #f4f4f4;
    --illus-mid: #cfcfcf;
    --illus-dark: #9d9d9d;
  }
  * { box-sizing: border-box; margin: 0; padding: 0; }
  html, body { width: 1200px; height: 491px; overflow: hidden; background: var(--bg); }
  body { position: relative; font-family: "Questrial", sans-serif; color: var(--grey-text); }

  .postcard {
    position: absolute; top: 30px; width: 564px; height: 432px;
    background: var(--card); box-shadow: 0 2px 6px rgba(0,0,0,.25);
  }
  .postcard--front { left: 26px; }
  .postcard--back { left: 612px; }
  .abs { position: absolute; }

  /* brand lockup */
  .brand { display: flex; align-items: center; gap: 10px; }
  .brand__mark { border: 3px solid var(--purple); border-radius: 4px; }
  .brand__name { color: var(--purple); line-height: 1; text-transform: uppercase; }
  .brand__name span { display: block; color: var(--grey-mid); }
  .front-brand { left: 30px; top: 20px; }
  .front-brand .brand__mark { width: 62px; height: 62px; }
  .front-brand .brand__name { font-size: 21px; letter-spacing: .5px; }
  .front-brand .brand__name span { margin-top: 6px; font-size: 16px; }

  .follow { left: 386px; top: 48px; display: flex; align-items: center; gap: 6px; font-size: 12px; color: #222; }
  .follow__net { font-size: 9px; color: var(--grey-mid); }

  .offer-band {
    left: 26px; top: 104px; width: 324px; height: 232px; background: var(--purple);
    box-shadow: 0 12px 10px -6px rgba(0,0,0,.25);
  }
  .offer-band__headline {
    position: absolute; left: 28px; top: 44px; color: #fff;
    font-size: 26px; line-height: 34px;
  }
  .offer-photo {
    left: 350px; top: 104px; width: 192px; height: 232px;
    border: 1px solid #4d3d8a;
    background: radial-gradient(ellipse at 50% 40%, var(--photo-light) 0%, var(--photo-dark) 75%, #2a2220 100%);
  }
  .offer-price {
    left: 28px; top: 358px; color: var(--purple); font-size: 19px; line-height: 28px; letter-spacing: .4px;
  }
  .offer-price .bigger { font-size: 23px; }
  .offer-price .only { font-family: "Arimo", sans-serif; font-weight: 700; font-size: 22px; letter-spacing: 0; }
  .offer-price .amount { font-family: "Arimo", sans-serif; font-weight: 700; font-size: 38px; letter-spacing: 0; }

  .partner { left: 462px; top: 378px; display: flex; align-items: center; gap: 6px; }
  .partner__mark { width: 22px; height: 22px; background: var(--partner-blue); }
  .partner__name { color: var(--partner-blue); font-size: 20px; }

  /* back */
  .back-brand { left: 58px; top: 23px; }
  .back-brand .brand__mark { width: 36px; height: 36px; border-color: var(--grey-mid); border-width: 2px; }
  .back-brand .brand__name { font-size: 14px; color: #444; }
  .back-brand .brand__name span { margin-top: 3px; font-size: 10px; }

  .glasses-art {
    left: 22px; top: 108px; width: 270px; height: 248px;
    background: radial-gradient(ellipse at 50% 38%, var(--illus-light) 0%, var(--illus-mid) 60%, var(--illus-dark) 100%);
  }
  .contact-list { left: 62px; top: 368px; list-style: none; font-size: 15px; line-height: 17.5px; color: #222; }
  .contact-list li { display: flex; align-items: center; gap: 8px; }
  .contact-list svg { width: 12px; height: 12px; }

  .divider { left: 309px; top: 0; width: 1px; height: 432px; background: #d8d8d8; }
  .return-address { left: 323px; top: 23px; font-size: 12px; line-height: 16px; color: #222; }
  .postage {
    left: 456px; top: 25px; width: 82px; height: 93px; border: 1px solid #555;
    font-family: "Arimo", sans-serif; font-size: 9.5px; line-height: 12px; text-align: center; padding-top: 8px; color: #222;
  }
  .postage strong { display: block; }
  .recipient { left: 332px; top: 180px; font-size: 14px; color: #222; }
  .address-line { left: 332px; width: 212px; height: 1px; background: var(--rule); }
  .address-line--1 { top: 215px; }
  .address-line--2 { top: 256px; }
  .address-line--3 { top: 298px; }
</style>
</head>
<body>

<section class="postcard postcard--front">
  <div class="brand front-brand abs">
    <div class="brand__mark"></div>
    <div class="brand__name">Pennrock Optic<span>Associates</span></div>
  </div>

  <div class="follow abs">Follow Us
    <span class="follow__net">quillo</span>
    <span class="follow__net">frendlio</span>
    <span class="follow__net">m+</span>
  </div>

  <div class="offer-band abs">
    <p class="offer-band__headline">Buy a Year Supply of<br>Contact Lenses<br>and Get&nbsp; a Complete<br>Pair of Glasses</p>
  </div>
  <div class="offer-photo abs" role="img" aria-label="Photo of a young woman wearing black rectangular glasses"></div>

  <p class="offer-price abs">New Frame, Vorne Lenses,<br>1 Year Warranty&nbsp; <span class="bigger">all this for</span> <span class="only">Only</span> <span class="amount">$59</span></p>

  <div class="partner abs">
    <div class="partner__mark"></div>
    <span class="partner__name">Vorne</span>
  </div>
</section>

<section class="postcard postcard--back">
  <div class="brand back-brand abs">
    <div class="brand__mark"></div>
    <div class="brand__name">Pennrock Optic<span>Associates</span></div>
  </div>

  <div class="glasses-art abs" role="img" aria-label="Large grey illustration of an eye inside a rounded square, resting on a pair of rectangular glasses"></div>

  <ul class="contact-list abs">
    <li><svg viewBox="0 0 12 12"><circle cx="6" cy="6" r="5.3" fill="none" stroke="#222" stroke-width="1"/><path d="M4 3.5l1.2 1.4-.6.8c.4.8 1 1.4 1.8 1.8l.8-.6 1.4 1.2-.8 1c-2 0-4.5-2.5-4.6-4.6z" fill="#222"/></svg>(555) 014-2020</li>
    <li><svg viewBox="0 0 12 12"><rect x="1" y="3" width="10" height="7" fill="none" stroke="#222"/><path d="M1 3l5 4 5-4" fill="none" stroke="#222"/></svg>info@pennrockoptic.com</li>
    <li><svg viewBox="0 0 12 12"><circle cx="6" cy="6" r="5" fill="none" stroke="#222"/><ellipse cx="6" cy="6" rx="2" ry="5" fill="none" stroke="#222"/><path d="M1 6h10" stroke="#222"/></svg>www.pennrockoptic.com</li>
  </ul>

  <div class="divider abs"></div>

  <p class="return-address abs">PENNROCK OPTIC<br>880 Larkfield Ave<br>Suite 4<br>Pennrock, VA 24999</p>

  <div class="postage abs">Presorted<br>First Class Mail<br>US Postage<strong>PAID</strong>Fairview, CA<br>Permit #4821</div>

  <p class="recipient abs">To,</p>
  <div class="address-line address-line--1 abs"></div>
  <div class="address-line address-line--2 abs"></div>
  <div class="address-line address-line--3 abs"></div>
</section>

</body>
</html>
```